MARBLED SPARROW WEB DESIGN PROJECT

We are a brand new company called "Marbled Sparrow" which specialise in one-off Vintage Clothing. We would like somebody to design a web page which will be the sole income for our company. Our main aim is to have an easy searchable website which is user friendly. The key to the website is to target people who do not like the idea of op-shopping but love vintage clothes - this website will be the answer.
Updates

This website will need to be coded to work with Tin Lantern - Please read this before you start. https://help.tinlantern.example/articles/Public/How-do-I-create-custom-template-files-for-my-store

Hi everyone, Just want to make note that the this website is for young people. Just so people a clear I want modern young people dressed in Vintage clothes as this is that reality and what they would like to see. Not people dressed like they are going to a fancy dress party, i.e. dresses like it was that era. Thanks Mirela

Coding

Coded - Design and coding required

```html
<!DOCTYPE html>
<html lang="en">
<head>
<meta charset="utf-8">
<title>Marbled Sparrow — Vintage Clothing</title>
<link rel="stylesheet" href="https://fonts.googleapis.com/css2?family=Open+Sans:wght@400;600;700&family=Oswald:wght@300;400;600&family=Playfair+Display:wght@400;700&display=swap">
<style>
:root{
  --green:#76b53f;
  --navy:#0f3a6b;
  --ink:#444;
  --muted:#777;
  --line:#d8d8d8;
  --pink:#f8e8e6;
  --strip:#f1f1f1;
  --white:#fff;
  --steel:#7f9ab6;
  --mist:#c5d1de;
}
*{box-sizing:border-box;margin:0;padding:0}
html,body{width:730px;height:1200px;overflow:hidden;background:var(--white)}
body{position:relative;font-family:"Open Sans",sans-serif;color:var(--ink)}
.abs{position:absolute}
a{color:inherit;text-decoration:none}

/* header */
.brand{left:94px;top:14px;font-family:"Oswald",sans-serif;font-weight:600;color:var(--navy);font-size:25px;line-height:25px;letter-spacing:.5px}
.search{left:312px;top:13px;width:144px;height:21px;border:1px solid #bbb;font-size:7px;font-style:italic;color:#999;padding:5px 7px}
.account{left:559px;top:17px;font-size:9px;color:var(--navy)}
.account span{margin:0 10px;color:#ccc}
.nav{top:56px;font-size:8.5px;font-weight:600;color:var(--navy);text-transform:uppercase}
.nav.active{color:var(--green)}
.nav-sep{top:52px;width:1px;height:18px;background:#ccc;transform:skewX(-25deg)}

/* hero */
.hero-bg{left:0;top:78px;width:400px;height:252px;background:var(--pink)}
.hero-photo{left:400px;top:78px;width:330px;height:252px;background:linear-gradient(135deg,#6f6b66,#a9a49c 55%,#55524e)}
.hero-title{left:94px;top:126px;font-family:"Playfair Display",serif;font-weight:700;color:var(--green);font-size:24.5px;letter-spacing:.2px;white-space:nowrap}
.hero-upto{left:93px;top:225px;transform:rotate(-90deg);transform-origin:left top;font-family:"Playfair Display",serif;font-weight:700;color:var(--navy);font-size:16px;letter-spacing:1px;white-space:nowrap}
.hero-pct{left:114px;top:148px;font-family:"Playfair Display",serif;font-weight:700;color:var(--green);font-size:80px;line-height:1;letter-spacing:-2px}
.hero-off{left:301px;top:225px;transform:rotate(-90deg);transform-origin:left top;font-family:"Playfair Display",serif;font-weight:700;color:var(--navy);font-size:22px;letter-spacing:2px}
.btn{left:96px;top:251px;width:79px;height:22px;background:var(--green);color:var(--white);font-family:"Playfair Display",serif;font-weight:700;font-size:10.5px;text-align:center;line-height:22px}

/* category tiles */
.tile{background:linear-gradient(135deg,#5a4c40,#a08a72)}
.tile-label{font-family:"Oswald",sans-serif;font-weight:300;color:var(--white);font-size:16px;line-height:18px;text-align:right}

/* feature */
.section-title{left:94px;top:522px;font-size:13px;font-weight:700;color:var(--navy);letter-spacing:.3px}
.section-rule{left:238px;top:529px;width:370px;height:3px;background:#e2e2e2}
.product-img{width:127px;height:106px}
.product-cap{width:127px;height:39px;border:1px solid var(--line);font-size:8px;padding:6px 8px;line-height:14px;color:var(--muted)}
.product-cap b{display:block;color:var(--navy);font-weight:600}
.product-cap.first{color:var(--green)}

/* promos */
.promo{width:168px;height:177px}
.promo-tag{width:150px;height:24px;border:1px solid var(--white);background:rgba(255,255,255,.85);font-size:8.5px;font-weight:600;color:var(--navy);padding:0 10px;line-height:22px}
.promo-tag svg{position:absolute;right:10px;top:7px}
.vip{font-family:"Oswald",sans-serif;font-weight:300;color:var(--white);font-size:12.5px;text-align:right;white-space:nowrap}
.vip-pct{left:543px;top:820px;font-family:"Playfair Display",serif;font-style:italic;font-weight:700;color:var(--green);font-size:38px;line-height:1}
.vip-off{left:605px;top:866px;transform:rotate(-65deg);transform-origin:left top;font-family:"Oswald",sans-serif;font-weight:600;color:var(--white);font-size:14px;line-height:1}

/* banner */
.banner-end{top:914px;width:66px;height:46px}
.banner{left:160px;top:914px;width:408px;height:46px;background:var(--green);color:var(--white);font-size:9.6px;font-weight:600;text-align:center;line-height:14px;padding-top:9px}

/* perks */
.strip{left:0;top:981px;width:730px;height:187px;background:var(--strip)}
.perks{left:94px;top:981px;width:542px;height:63px;background:var(--white)}
.perk-title{font-size:10.5px;font-weight:700;letter-spacing:.3px}
.perk-text{font-size:8px;color:var(--ink)}

/* footer */
.foot-h{top:1059px;font-size:8.5px;font-weight:600;color:var(--navy)}
.foot-h::after{content:"";display:block;width:70px;height:1px;background:#ccc;margin-top:4px}
.foot-list{top:1080px;font-size:7px;line-height:13.6px;color:var(--ink);list-style:none}
.foot-list.nav-list li:first-child{color:var(--navy)}
.foot-div{top:1056px;width:1px;height:112px;background:#cfd5dd}
.news-text{left:491px;top:1080px;width:150px;font-size:7px;line-height:11px}
.news-field{left:491px;top:1108px;width:145px;height:20px;border:1px solid #ccc;background:var(--white);font-size:7px;padding:5px 8px;color:#555}
.news-go{left:615px;top:1108px;width:21px;height:20px;background:var(--green)}
.social{top:1141px;width:10px;height:10px;border-radius:50%;background:#b7bdc6}
.social-sep{top:1138px;width:1px;height:16px;background:#ddd}

/* bottom bar */
.bottom{left:0;top:1168px;width:730px;height:32px;background:var(--navy)}
.card{top:1176px;width:20px;height:14px;border-radius:2px;background:#e8e8e8}
.copy{left:518px;top:1180px;font-size:7px;color:#b8c4d4}
.copy b{color:var(--white);font-weight:600}
</style>
</head>
<body>

<!-- header -->
<div class="abs brand">MARBLED<br>SPARROW</div>
<div class="abs search">Search entire shop here...</div>
<div class="abs account"><a href="#">Login</a><span>/</span><a href="#">Register</a></div>

<a class="abs nav active" style="left:312px" href="#">Home</a>
<div class="abs nav-sep" style="left:349px"></div>
<a class="abs nav" style="left:359px" href="#">Women</a>
<div class="abs nav-sep" style="left:404px"></div>
<a class="abs nav" style="left:415px" href="#">Men</a>
<div class="abs nav-sep" style="left:446px"></div>
<a class="abs nav" style="left:457px" href="#">Style Tips</a>
<div class="abs nav-sep" style="left:511px"></div>
<a class="abs nav" style="left:522px" href="#">FAQs</a>
<div class="abs nav-sep" style="left:556px"></div>
<div class="abs nav" style="left:589px;top:55px;text-transform:none;font-weight:400">
  <svg width="14" height="11" viewBox="0 0 14 11" style="vertical-align:-2px"><path d="M0 1h2.5l2 6.5h7l1.5-4.5H4" fill="none" stroke="#0f3a6b" stroke-width="1.3"/><circle cx="5.5" cy="9.6" r="1" fill="#0f3a6b"/><circle cx="10.5" cy="9.6" r="1" fill="#0f3a6b"/></svg>
  Cart <span style="font-size:6px">&#9660;</span>
</div>
<div class="abs" style="left:597px;top:53px;font-size:7px;font-weight:700;color:var(--green)">0</div>

<!-- hero -->
<div class="abs hero-bg" role="img" aria-label="Soft pink floral pattern background"></div>
<div class="abs hero-photo" role="img" aria-label="Photo of a young woman in a grey lace vintage dress against a stone wall"></div>
<div class="abs hero-title">VINTAGE CLOTHING</div>
<div class="abs hero-upto">UP TO</div>
<div class="abs hero-pct">20%</div>
<div class="abs hero-off">OFF</div>
<a class="abs btn" href="#">SHOP NOW</a>

<!-- category tiles -->
<div class="abs tile" style="left:94px;top:353px;width:259px;height:149px" role="img" aria-label="Photo of a young woman in a plaid shirt and sunglasses sitting on a wooden floor"></div>
<div class="abs tile-label" style="left:260px;top:453px;width:84px">SHOP<br>WOMEN'S</div>
<div class="abs tile" style="left:376px;top:353px;width:259px;height:149px;background:linear-gradient(135deg,#c9c5bd,#3d3b38)" role="img" aria-label="Photo of a young man in a light blazer beside vintage cars"></div>
<div class="abs tile-label" style="left:540px;top:453px;width:86px">SHOP<br>MEN'S</div>

<!-- feature products -->
<div class="abs section-title">FEATURE PRODUCTS</div>
<div class="abs section-rule"></div>
<svg class="abs" style="left:612px;top:525px" width="24" height="9" viewBox="0 0 24 9">
  <path d="M0 4.5 4.5 0v3h5v3h-5v3z" fill="#8a8a8a"/>
  <path d="M24 4.5 19.5 0v3h-5v3h5v3z" fill="#76b53f"/>
</svg>

<div class="abs product-img" style="left:94px;top:549px;background:linear-gradient(135deg,#7d7872,#b2ada5)" role="img" aria-label="Product photo of a grey lace party dress"></div>
<div class="abs product-cap first" style="left:94px;top:656px">1950s Party Dress<b>Only: $25</b></div>

<div class="abs product-img" style="left:232px;top:549px;background:linear-gradient(135deg,#8d7c6a,#3f3832)" role="img" aria-label="Product photo of a man in an open cardigan"></div>
<div class="abs product-cap" style="left:232px;top:656px">1950s Party Dress<b>Only: $25</b></div>

<div class="abs product-img" style="left:370px;top:549px;background:linear-gradient(135deg,#2c4a63,#6d8ea2)" role="img" aria-label="Product photo of red heels and a printed skirt"></div>
<div class="abs product-cap" style="left:370px;top:656px">1950s Party Dress<b>Only: $25</b></div>

<div class="abs product-img" style="left:509px;top:549px;background:linear-gradient(135deg,#a6b04a,#c44f8a)" role="img" aria-label="Product photo of a colourful printed top with bangles"></div>
<div class="abs product-cap" style="left:509px;top:656px">1950s Party Dress<b>Only: $25</b></div>

<!-- promos -->
<div class="abs promo" style="left:94px;top:715px;background:linear-gradient(135deg,#d8d4d3,#7b7471)" role="img" aria-label="Photo of a smiling young woman in a grey cardigan in a clothing shop"></div>
<div class="abs promo-tag" style="left:102px;top:861px">STYLE TIPS
  <svg width="10" height="8" viewBox="0 0 10 8"><path d="M10 4 6 0v2.5H0v3h6V8z" fill="#888"/></svg></div>

<div class="abs promo" style="left:281px;top:715px;background:linear-gradient(135deg,#5d7184,#1c1f24)" role="img" aria-label="Photo of a young couple in denim lounging together"></div>
<div class="abs promo-tag" style="left:290px;top:861px;background:rgba(255,255,255,.75)">SHOP ERA
  <svg width="10" height="8" viewBox="0 0 10 8"><path d="M10 4 6 0v2.5H0v3h6V8z" fill="#888"/></svg></div>

<div class="abs promo" style="left:468px;top:715px;background:linear-gradient(135deg,#5a4a43,#1b1a1a 60%)" role="img" aria-label="Photo of a young woman in a peach vintage dress and sunglasses"></div>
<div class="abs vip" style="left:520px;top:784px;width:107px;line-height:19px">JOIN OUR VIP<br>CLUB AND RECEIVE</div>
<div class="abs vip-pct">50%</div>
<div class="abs vip-off">OFF</div>
<div class="abs vip" style="left:520px;top:866px;width:106px;font-style:italic;font-weight:400">EVERY ORDER!</div>

<!-- banner -->
<div class="abs banner-end" style="left:94px;background:linear-gradient(90deg,var(--mist),var(--steel) 45%,var(--navy))" role="img" aria-label="Decorative cluster of overlapping hearts in blue tones"></div>
<div class="abs banner">MARBLED SPARROW IS ALL ABOUT BEING DIFFERENT. THAT'S WAY ALL<br>OUR CLOTHES ARE UNIQUE, SO YOU CAN BE DAZZLING DIFFERENT</div>
<div class="abs banner-end" style="left:568px;width:68px;background:linear-gradient(90deg,var(--navy),var(--steel) 55%,var(--mist))" role="img" aria-label="Decorative cluster of overlapping hearts in blue tones"></div>

<!-- perks -->
<div class="abs strip"></div>
<div class="abs perks"></div>

<svg class="abs" style="left:109px;top:995px" width="36" height="36" viewBox="0 0 36 36">
  <circle cx="18" cy="18" r="17" fill="none" stroke="#0f3a6b" stroke-width="1.5"/>
  <path d="M9 13h12v10H9zM21 16h4l3 3.5V23h-7z" fill="#0f3a6b"/>
  <circle cx="13" cy="24" r="2" fill="#0f3a6b" stroke="#fff"/><circle cx="24.5" cy="24" r="2" fill="#0f3a6b" stroke="#fff"/>
</svg>
<div class="abs perk-title" style="left:155px;top:998px;color:var(--navy)">FREE SHIPPING</div>
<div class="abs perk-text" style="left:157px;top:1016px">RM On order over $ 100</div>

<svg class="abs" style="left:280px;top:995px" width="36" height="36" viewBox="0 0 36 36">
  <circle cx="18" cy="18" r="17" fill="none" stroke="#76b53f" stroke-width="1.5"/>
  <circle cx="18" cy="18" r="11" fill="none" stroke="#76b53f" stroke-width="1.5" stroke-dasharray="30 5"/>
  <text x="18" y="23" text-anchor="middle" font-family="Open Sans,sans-serif" font-weight="700" font-size="13" fill="#76b53f">$</text>
</svg>
<div class="abs perk-title" style="left:325px;top:998px;color:var(--green)">15 DAYS FREE RETURN</div>
<div class="abs perk-text" style="left:328px;top:1016px">Lorem Ispum Dolor sit On day</div>

<svg class="abs" style="left:476px;top:995px" width="36" height="36" viewBox="0 0 36 36">
  <circle cx="18" cy="18" r="17" fill="none" stroke="#76b53f" stroke-width="1.5"/>
  <path d="M18 8v20M9.5 13l17 10M26.5 13l-17 10" stroke="#76b53f" stroke-width="2.5" stroke-linecap="round"/>
</svg>
<div class="abs perk-title" style="left:521px;top:998px;color:var(--green)">100% ORIGINAL</div>
<div class="abs perk-text" style="left:523px;top:1016px">Lorem Ispum Dolor Amet</div>

<!-- footer -->
<div class="abs foot-h" style="left:94px">MARBLED SPARROW</div>
<ul class="abs foot-list nav-list" style="left:94px">
  <li>Home</li><li>About Us</li><li>Terms of use</li><li>Privacy Policy</li><li>Press</li><li>Contact Us</li>
</ul>
<div class="abs foot-div" style="left:206px"></div>

<div class="abs foot-h" style="left:231px">CONNECT WITH US</div>
<ul class="abs foot-list" style="left:231px">
  <li>My Account</li><li>Style Tips</li><li>FAQs</li><li>Shipping</li><li>Track Your Order</li><li>Size Chart</li>
</ul>
<div class="abs foot-div" style="left:336px"></div>

<div class="abs foot-h" style="left:361px">CONNECT WITH US</div>
<ul class="abs foot-list" style="left:361px">
  <li>Men</li><li>Women</li><li>Accessories</li><li>Bags</li><li>Shoes</li>
</ul>
<ul class="abs foot-list" style="left:421px">
  <li>50S</li><li>60S</li><li>70S</li><li>80S</li><li>90S</li>
</ul>
<div class="abs foot-div" style="left:466px"></div>

<div class="abs foot-h" style="left:491px">NEWSLETTER</div>
<div class="abs news-text">Lorem ipsum dolor sit amet, consr adipi scing elit. Aliquam</div>
<div class="abs news-field">your@email.com</div>
<div class="abs news-go"><svg width="21" height="20" viewBox="0 0 21 20"><path d="M8 5l6 5-6 5z" fill="#fff"/></svg></div>

<div class="abs social" style="left:489px"></div>
<div class="abs social-sep" style="left:510px"></div>
<div class="abs social" style="left:521px"></div>
<div class="abs social-sep" style="left:542px"></div>
<div class="abs social" style="left:553px"></div>
<div class="abs social-sep" style="left:574px"></div>
<div class="abs social" style="left:585px"></div>
<div class="abs social-sep" style="left:606px"></div>
<div class="abs social" style="left:615px"></div>

<!-- bottom bar -->
<div class="abs bottom"></div>
<div class="abs card" style="left:94px"></div>
<div class="abs card" style="left:119px"></div>
<div class="abs card" style="left:144px"></div>
<div class="abs card" style="left:169px"></div>
<div class="abs card" style="left:194px"></div>
<div class="abs card" style="left:218px"></div>
<div class="abs copy">Copyright © 2015 <b>Marbled Sparrow</b>.</div>

</body>
</html>
```